Professional letterhead for engineering type firm.

I would like to have a professional looking letterhead for a small HVAC testing company/engineering-type firm. I would like to see designs that show a professional level of expertise and established company. Traditional letterhead designs are a good place to start.
We are a QRTV certified company (which is a big deal in our industry). I have included the QRTV logo, but would like the green in QRTV logo to be black.
Presently, we work out of house so i would not like to include our address at this point.
Information to include:
Phone: 410-555-0162
Website: www.Kestro-VUN.com
Email: Info@Kestro-VUN.com

```html
<!DOCTYPE html>
<html lang="en">
<head>
<meta charset="utf-8">
<title>Kestro VUN Letterhead</title>
<link rel="stylesheet" href="https://fonts.googleapis.com/css2?family=Lato:wght@400;700&family=Montserrat:wght@400;500&family=Italianno&display=swap">
<style>
  :root {
    --backdrop: #e4e5e7;
    --paper: #ffffff;
    --ink: #1c1c1c;
    --ink-soft: #2a2a2a;
    --brand-blue: #2f4ea8;
    --brand-blue-light: #3f8ad0;
    --brand-blue-deep: #27388f;
    --brand-red: #e41b23;
  }
  * { box-sizing: border-box; margin: 0; padding: 0; }
  html, body {
    width: 1200px; height: 874px; overflow: hidden;
    background: var(--backdrop);
  }
  .letterhead {
    position: absolute; left: 300px; top: 13px;
    width: 600px; height: 848px;
    background: var(--paper);
    box-shadow: 0 6px 24px rgba(0,0,0,.12);
    overflow: hidden;
    font-family: "Lato", sans-serif;
    color: var(--ink);
  }
  .brand {
    position: absolute; left: 48px; top: 52px;
    display: flex; align-items: center; gap: 10px;
  }
  .brand-dot {
    width: 22px; height: 22px; border-radius: 50%;
    background: var(--brand-blue);
  }
  .brand-name {
    font-family: "Lato", sans-serif; font-weight: 700;
    font-size: 24px; letter-spacing: 1px; color: var(--brand-blue);
  }
  .cert-badge {
    position: absolute; left: 250px; top: 44px;
    width: 62px; height: 40px; background: var(--ink);
    border-radius: 3px;
  }
  .contact {
    position: absolute; right: 36px; top: 40px;
    padding-left: 14px; border-left: 1.5px solid var(--brand-red);
    font-family: "Montserrat", sans-serif; font-style: normal;
    font-size: 9.5px; line-height: 15px; color: var(--ink-soft);
  }
  .contact-row { display: flex; align-items: center; gap: 6px; }
  .contact-row svg { width: 9px; height: 9px; flex: none; }
  .letter {
    position: absolute; left: 70px; top: 180px; width: 470px;
    font-size: 11px; line-height: 14.5px;
  }
  .letter-date { margin-bottom: 12px; font-size: 12px; }
  .recipient { margin-bottom: 14px; font-size: 11.5px; }
  .address { margin-bottom: 22px; font-size: 11.5px; }
  .salutation { font-weight: 700; font-size: 14px; margin-bottom: 18px; }
  .letter p.body { margin-bottom: 16px; }
  .closing { margin-top: 24px; font-size: 11.5px; }
  .signature {
    font-family: "Italianno", cursive; font-size: 44px;
    margin-top: 22px; margin-left: 40px; line-height: 1;
  }
  .footer-band {
    position: absolute; left: 0; bottom: 0; width: 600px; height: 56px;
    background: linear-gradient(90deg, var(--brand-blue-light), var(--brand-blue-deep) 60%, var(--brand-blue-light));
  }
</style>
</head>
<body>
  <main class="letterhead">
    <header>
      <div class="brand">
        <span class="brand-dot"></span>
        <span class="brand-name">KESTRO VUN</span>
      </div>
      <div class="cert-badge" role="img" aria-label="Certification badge"></div>
      <address class="contact">
        <div class="contact-row">
          <svg viewBox="0 0 10 10"><path d="M2 1 L4 1 L4.6 3 L3.4 4 Q4.5 6 6 6.6 L7 5.4 L9 6 L9 8 Q5 9 1 3 Z" fill="var(--brand-red)"/></svg>
          <span>410-555-0162</span>
        </div>
        <div class="contact-row">
          <svg viewBox="0 0 10 10"><rect x="1" y="2.5" width="8" height="5.5" fill="var(--brand-blue)"/><path d="M1 2.5 L5 5.5 L9 2.5" stroke="#fff" stroke-width=".8" fill="none"/></svg>
          <span>Info@Kestro-VUN.com</span>
        </div>
        <div class="contact-row">
          <svg viewBox="0 0 10 10"><circle cx="5" cy="5" r="4" fill="var(--brand-red)"/><path d="M1 5 H9 M5 1 Q2.5 5 5 9 M5 1 Q7.5 5 5 9" stroke="#fff" stroke-width=".7" fill="none"/></svg>
          <span>www.Kestro-VUN.com</span>
        </div>
      </address>
    </header>

    <section class="letter">
      <p class="letter-date">January-03-2020</p>
      <p class="recipient">Mr. Dale Porter<br>President</p>
      <p class="address">Fenwick Group<br>48 Harbor Lane, Suite# 10<br>City, State, 120023</p>
      <p class="salutation">Dear Mr. Porter</p>
      <p class="body">Lorem ipsum dolor sit amet, consectetur adipiscing elit, sed do eiusmod tempor incididunt ut labore et dolore magna aliqua. Ut enim ad minim veniam, quis nostrud exercitation ullamco laboris nisi ut aliquip ex ea commodo consequat. Duis aute irure dolor in reprehenderit in voluptate velit esse cillum dolore eu fugiat nulla pariatur.</p>
      <p class="body">Lorem ipsum dolor sit amet, consectetur adipiscing elit, sed do eiusmod tempor incididunt ut labore et dolore magna aliqua. Ut enim ad minim veniam, quis nostrud exercitation ullamco laboris nisi ut aliquip ex ea commodo consequat. Duis aute irure dolor in reprehenderit in voluptate velit esse cillum dolore eu fugiat nulla pariatur.</p>
      <p class="body">Lorem ipsum dolor sit amet, consectetur adipiscing elit, sed do eiusmod tempor incididunt ut labore et dolore magna aliqua. Ut enim ad minim veniam, quis nostrud exercitation ullamco laboris nisi ut aliquip ex ea commodo consequat.</p>
      <p class="body">Excepteur sint occaecat cupidatat non proident, sunt in culpa qui officia deserunt mollit anim id est laborum. re et dolore magnam aliquam quaerat voluptatem.</p>
      <p class="closing">Regards</p>
      <p class="signature">Marcus Hale</p>
    </section>

    <div class="footer-band" role="img" aria-label="Decorative footer wave in blue with a red stripe"></div>
  </main>
</body>
</html>
```